Professional/Sleek card design for athletic apparel brand

Athletic apparel brand. Mainly focused on lifting weights/gym workouts. Logo and brand are already created. Must use brand logo and name. Creativity is welcome. Looking for a clean, modern, and sexy design.

```html
<!DOCTYPE html>
<html lang="en">
<head>
<meta charset="utf-8">
<title>Iron and Grit – Business Card</title>
<link href="https://fonts.googleapis.com/css2?family=Open+Sans:wght@400;700&display=swap" rel="stylesheet">
<style>
  :root {
    --stage: #232323;
    --card: #1d1d1d;
    --card-back: #141414;
    --ink: #ffffff;
    --ink-soft: #e6e6e6;
  }
  * { margin: 0; padding: 0; box-sizing: border-box; }
  html, body {
    width: 1200px; height: 780px; overflow: hidden;
    background: var(--stage);
    font-family: "Open Sans", Arial, sans-serif;
    color: var(--ink);
  }
  .stage { position: relative; width: 1200px; height: 780px; }
  .card {
    position: absolute; top: 90px;
    width: 343px; height: 600px;
    border-radius: 26px;
    overflow: hidden;
    box-shadow: 0 18px 40px rgba(0,0,0,.55);
  }
  .card--back { left: 230px; background: var(--card-back); }
  .card--front { left: 627px; background: var(--card); }

  .pattern-field {
    position: absolute; inset: 0;
    background: linear-gradient(150deg, #6a6a6a 0%, #2c2c2c 32%, #111111 60%, #0c0c0c 100%);
  }
  .back-brand {
    position: absolute; right: 30px; bottom: 30px;
    display: flex; align-items: center; gap: 6px;
    font-weight: 700; font-size: 11px; letter-spacing: .04em;
    text-transform: uppercase; color: var(--ink);
  }
  .brand-dot {
    width: 10px; height: 10px; border-radius: 50%; background: var(--ink);
  }

  .front-brand {
    position: absolute; top: 80px; left: 0; right: 0;
    display: flex; flex-direction: column; align-items: center; gap: 16px;
  }
  .front-brand .brand-dot { width: 64px; height: 64px; }
  .brand-name {
    font-weight: 700; font-size: 26px; letter-spacing: .06em;
    text-transform: uppercase; color: var(--ink);
  }
  .identity {
    position: absolute; top: 330px; left: 0; right: 0; text-align: center;
  }
  .person-name { font-weight: 700; font-size: 26px; line-height: 1.1; }
  .person-title { font-size: 15px; color: var(--ink-soft); margin-top: 4px; }

  .address {
    position: absolute; top: 420px; left: 40px;
    font-size: 14px; line-height: 1.35; color: var(--ink-soft); font-style: normal;
  }
  .contacts {
    position: absolute; top: 478px; left: 40px;
    list-style: none; font-size: 12.5px; line-height: 1.6; color: var(--ink-soft);
  }
  .contacts li { display: flex; align-items: center; gap: 8px; }
  .contacts svg { width: 12px; height: 12px; flex: none; fill: none; stroke: var(--ink); stroke-width: 1.6; }
</style>
</head>
<body>
<main class="stage">
  <section class="card card--back">
    <div class="pattern-field" role="img" aria-label="Repeating brand-mark pattern with a glossy highlight across the top corner"></div>
    <div class="back-brand"><span class="brand-dot"></span>Iron and Grit</div>
  </section>

  <section class="card card--front">
    <div class="front-brand">
      <span class="brand-dot"></span>
      <span class="brand-name">Iron and Grit</span>
    </div>

    <div class="identity">
      <h1 class="person-name">Marcus Delane</h1>
      <p class="person-title">Founder &amp; CEO</p>
    </div>

    <address class="address">
      4820 E Ridge Ave. Ste. 210<br>
      Mesa, AZ 85201
    </address>

    <ul class="contacts">
      <li>
        <svg viewBox="0 0 12 12"><rect x="3" y="1" width="6" height="10" rx="1"/></svg>
        (480) 555-0142
      </li>
      <li>
        <svg viewBox="0 0 12 12"><path d="M2 2c0 5 3 8 8 8l1-2-2-1-1 1C6 7 5 6 4 4l1-1-1-2z"/></svg>
        1 (800) 555-0199 Ext. 120
      </li>
      <li>
        <svg viewBox="0 0 12 12"><circle cx="6" cy="6" r="5"/><path d="M1 6h10M6 1c-2 3-2 7 0 10M6 1c2 3 2 7 0 10"/></svg>
        www.ironandgritapparel.com
      </li>
      <li>
        <svg viewBox="0 0 12 12"><rect x="1" y="2.5" width="10" height="7"/><path d="M1 2.5l5 4 5-4"/></svg>
        mdelane@ironandgritapparel.com
      </li>
    </ul>
  </section>
</main>
</body>
</html>
```